International wholesale business needs a business card

We need a business card.

Company Details:
Company Name and logo
Address, Phone number, Website
Employee Details:
Name, Designation, Mobile Number & Email address

```html
<!DOCTYPE html>
<html lang="en">
<head>
<meta charset="utf-8">
<title>Korvane Trading – Business Card</title>
<link href="https://fonts.googleapis.com/css2?family=Cinzel:wght@700&family=Questrial&display=swap" rel="stylesheet">
<style>
  :root {
    --bg: #d9d9d9;
    --brand-red: #c1272d;
    --brand-red-dark: #a81f25;
    --ink-grey: #7d7f82;
    --rule-grey: #c9c9c9;
    --swoosh-grey: #a7a9ac;
    --paper: #ffffff;
  }
  * { box-sizing: border-box; margin: 0; padding: 0; }
  html, body { width: 1200px; height: 852px; overflow: hidden; }
  body {
    background: var(--bg);
    position: relative;
    font-family: "Questrial", Arial, sans-serif;
  }
  .card {
    position: absolute;
    width: 520px;
    height: 300px;
    border-radius: 16px;
    overflow: hidden;
    box-shadow: 0 6px 18px rgba(0,0,0,.22);
  }

  /* Front */
  .card-front {
    left: 90px; top: 90px;
    background: var(--brand-red);
    color: var(--paper);
  }
  .front-brand {
    position: absolute;
    left: 0; right: 0; top: 108px;
    display: flex; align-items: center; justify-content: center; gap: 12px;
  }
  .brand-dot {
    width: 34px; height: 34px; border-radius: 50%;
    background: var(--paper);
  }
  .brand-name {
    font-family: "Cinzel", Georgia, serif;
    font-weight: 700;
    line-height: 1;
  }
  .front-brand .brand-name { font-size: 44px; letter-spacing: 1px; }
  .front-url {
    position: absolute; left: 0; right: 0; bottom: 44px;
    text-align: center;
    font-family: "Cinzel", Georgia, serif;
    font-size: 13px; letter-spacing: 6px;
  }

  /* Back */
  .card-back {
    left: 590px; top: 450px;
    background: var(--paper);
  }
  .back-brand {
    position: absolute; left: 32px; top: 46px;
    display: flex; align-items: center; gap: 10px;
  }
  .back-brand .brand-dot { width: 30px; height: 30px; background: var(--brand-red); }
  .back-brand .brand-name { font-size: 34px; color: var(--brand-red); }
  .divider {
    position: absolute; left: 32px; right: 32px; top: 112px;
    height: 1px; background: var(--rule-grey);
  }
  .address {
    position: absolute; right: 32px; top: 124px;
    text-align: right;
    font-size: 12.5px; line-height: 1.45;
    color: var(--brand-red);
  }
  .person { position: absolute; left: 32px; top: 138px; }
  .person-name {
    font-family: "Cinzel", Georgia, serif;
    font-weight: 700; font-size: 19px;
    color: var(--brand-red);
  }
  .person-role {
    font-size: 12.5px; letter-spacing: .5px;
    color: var(--ink-grey); margin-top: 2px;
  }
  .contacts { list-style: none; margin-top: 10px; }
  .contacts li {
    display: flex; align-items: center; gap: 8px;
    font-size: 13px; color: var(--brand-red);
    margin-bottom: 4px;
  }
  .contact-icon {
    width: 15px; height: 15px; border-radius: 50%;
    background: var(--ink-grey);
    display: flex; align-items: center; justify-content: center;
  }
  .wave { position: absolute; left: 0; bottom: 0; width: 520px; height: 300px; }
  .back-url {
    position: absolute; left: 32px; bottom: 12px;
    font-size: 13px; color: var(--paper);
  }
</style>
</head>
<body>

  <section class="card card-front" aria-label="Card front">
    <div class="front-brand">
      <span class="brand-dot"></span>
      <span class="brand-name">Korvane Trading</span>
    </div>
    <p class="front-url">WWW.KORVANETRADING.COM</p>
  </section>

  <section class="card card-back" aria-label="Card back">
    <svg class="wave" viewBox="0 0 520 300" aria-hidden="true">
      <path d="M300 262 C400 236 470 200 520 150 L520 162 C470 210 400 246 300 262 Z" fill="var(--swoosh-grey)"/>
      <path d="M0 300 L0 258 C160 262 360 236 520 170 L520 300 Z" fill="var(--brand-red)"/>
    </svg>

    <div class="back-brand">
      <span class="brand-dot"></span>
      <span class="brand-name">Korvane Trading</span>
    </div>

    <div class="divider"></div>

    <p class="address">88 Larkfield Road<br>Suite 210, Brookhaven<br>OH 44102</p>

    <div class="person">
      <p class="person-name">DANIEL REYES</p>
      <p class="person-role">CEO/FOUNDER</p>
      <ul class="contacts">
        <li>
          <span class="contact-icon">
            <svg width="9" height="9" viewBox="0 0 10 10"><path d="M2 1 L4 1 L4.6 3 L3.4 4 C4 5.3 4.7 6 6 6.6 L7 5.4 L9 6 L9 8 C5 8.6 1.4 5 2 1 Z" fill="#fff"/></svg>
          </span>555-013-4827
        </li>
        <li>
          <span class="contact-icon">
            <svg width="9" height="9" viewBox="0 0 10 10"><rect x="3" y="1" width="4" height="8" rx="1" fill="#fff"/></svg>
          </span>555-013-4827
        </li>
        <li>
          <span class="contact-icon">
            <svg width="9" height="9" viewBox="0 0 10 10"><rect x="1" y="2.5" width="8" height="5" fill="#fff"/><path d="M1 2.5 L5 5.5 L9 2.5" stroke="#7d7f82" stroke-width=".8" fill="none"/></svg>
          </span>daniel@korvanemail.com
        </li>
      </ul>
    </div>

    <p class="back-url">www.korvanetrading.com</p>
  </section>

</body>
</html>
```